Hip Music Management Co. BIz Card

I have a logo (attached) the back side of the card should the full logo on the entire card- that's it. The front side of the card should show the logo somewhere, keeping with the 4 different shades of blue. The front side of the card can be a white background with logo and colored typeface for all info. Pretty simple.

Target Market(s)

I manage and produce a whole bunch of major label and indie artists.

Industry/Entity Type

Management

Contact Information for Business Card

Velmora Sound House (logo)
Dale Fornwick
President
www.velmorasoundhouse.com
dale@velmorasoundhouse.com
+1 310.555.7182
418 Willow Bend Lane
Ashgrove Falls, NY 10599

Requirements
Must have
• Entire logo on back side. White background on front- unless you provide something more interesting.
Nice to have
• On the front of the card if you choose a white backgound, if possible take my logo without the blue background (over white) that would be cool.

```html
<!DOCTYPE html>
<html lang="en">
<head>
<meta charset="utf-8">
<title>Velmora Sound House – Business Card</title>
<link rel="stylesheet" href="https://fonts.googleapis.com/css2?family=Montserrat:wght@500;600;700;800&display=swap">
<style>
  :root {
    --backdrop: #e9ebef;
    --navy: #141d52;
    --navy-edge: #1b2766;
    --teal: #1fb3c4;
    --sky: #4aa3dc;
    --blue: #2a7fc4;
    --title-blue: #3d8fd6;
    --name-grey: #6a6460;
    --ink-grey: #55575c;
    --card-white: #ffffff;
  }
  * { box-sizing: border-box; margin: 0; padding: 0; }
  html, body {
    width: 1200px; height: 900px; overflow: hidden;
    background: var(--backdrop);
    font-family: "Montserrat", Arial, sans-serif;
  }
  .canvas { position: relative; width: 1200px; height: 900px; }

  .card {
    position: absolute;
    width: 600px; height: 343px;
    border-radius: 18px;
    box-shadow: 0 10px 30px rgba(20, 29, 82, 0.18);
    overflow: hidden;
  }

  /* Back side: full-bleed wordmark */
  .card-back {
    left: 110px; top: 90px;
    background: linear-gradient(160deg, var(--navy-edge), var(--navy));
    display: flex; align-items: center; justify-content: center;
  }
  .card-back .wordmark {
    font-weight: 800;
    font-size: 48px;
    letter-spacing: 1px;
    color: var(--teal);
    text-transform: uppercase;
    text-align: center;
    line-height: 1.05;
  }

  /* Front side */
  .card-front {
    left: 490px; top: 467px;
    background: var(--card-white);
    padding: 40px 44px;
  }
  .card-front .wordmark {
    font-weight: 800;
    font-size: 26px;
    color: var(--teal);
    text-transform: uppercase;
    letter-spacing: 0.5px;
  }
  .person { position: absolute; left: 100px; top: 150px; }
  .person .name {
    font-weight: 600; font-size: 19px; color: var(--name-grey);
  }
  .person .title {
    font-weight: 600; font-size: 13px; color: var(--title-blue);
    margin-left: 82px; margin-top: 2px;
  }
  .contact {
    position: absolute; left: 300px; right: 40px; top: 172px;
    font-size: 10px; font-weight: 500; color: var(--ink-grey);
    line-height: 1.6;
    white-space: nowrap;
  }
  .contact .label { color: var(--title-blue); display: inline-block; width: 16px; }
  .contact .address { margin-top: 20px; }
</style>
</head>
<body>
<main class="canvas">
  <section class="card card-back" aria-label="Card back">
    <p class="wordmark">Velmora<br>Sound House</p>
  </section>

  <section class="card card-front" aria-label="Card front">
    <p class="wordmark">Velmora Sound House</p>

    <div class="person">
      <p class="name">Dale Fornwick</p>
      <p class="title">President</p>
    </div>

    <div class="contact">
      <p><span class="label">T:</span> +1 310.555.7182</p>
      <p><span class="label">W:</span> www.velmorasoundhouse.com</p>
      <p><span class="label">E:</span> dale@velmorasoundhouse.com</p>
      <p class="address"><span class="label">A:</span> 418 Willow Bend Lane Ashgrove Falls, NY 10599</p>
    </div>
  </section>
</main>
</body>
</html>
```